Adventure Business Cards

Please check out our website for style
Vertical card
Details:
Side 1
Logo
Business name: Kestrel Point Wildland Tours
Name: Colin Warbeck
Role: Director
Email: info@kestrelpointtours.com
Address: PO Box 71, Marlin Cove NSW 2471
Phone: +61 2 5550 1847
Web address: www.kestrelpointtours.com
Side 2
Taking pictures?
A Friendwall and Pixlane logo
Tag us in your pictures with
#kpwildtours
@kpwildtours
www.kestrelpointtours.com
Details:
Side 1
Logo
Name: Colin Warbeck
Role: Director
Phone: +61 2 5550 1847
Side 2
Taking pictures?
#kpwildtours
@kpwildtours

```html
<!DOCTYPE html>
<html lang="en">
<head>
<meta charset="utf-8">
<title>Kestrel Point Wildland Tours – Business Card</title>
<link rel="stylesheet" href="https://fonts.googleapis.com/css2?family=Amatic+SC:wght@700&family=Luckiest+Guy&family=Titan+One&display=block">
<style>
  :root {
    --page-bg: #e9e6e1;
    --forest-light: #8fa889;
    --forest-mid: #4d6b3f;
    --forest-dark: #141a10;
    --sky-top: #5f8fd6;
    --sky-bottom: #a9c3ea;
    --sea-top: #1f3f8c;
    --sea-bottom: #2b2f3a;
    --ink-light: #ffffff;
    --title-gold: #e9b44c;
    --title-blue: #4f86cf;
    --mark-ring: #1c1c1c;
    --card-shadow: rgba(0,0,0,0.35);
  }
  * { box-sizing: border-box; margin: 0; padding: 0; }
  html, body { width: 1200px; height: 1200px; overflow: hidden; }
  body {
    background: var(--page-bg);
    position: relative;
    font-family: "Amatic SC", "Arial Narrow", sans-serif;
    font-weight: 700;
    text-transform: uppercase;
    color: var(--ink-light);
  }
  .card {
    position: absolute;
    top: 150px;
    width: 500px;
    height: 900px;
    overflow: hidden;
    box-shadow: 0 10px 30px var(--card-shadow);
  }
  .card--front { left: 60px; }
  .card--back { left: 640px; }

  /* Front */
  .front-photo {
    position: absolute; inset: 0;
    background:
      radial-gradient(ellipse at 55% 30%, var(--forest-light) 0%, transparent 60%),
      linear-gradient(180deg, var(--forest-mid) 0%, #39522f 55%, var(--forest-dark) 100%);
  }
  .brand-mark {
    position: absolute; top: 70px; left: 0; right: 0;
    display: flex; flex-direction: column; align-items: center; gap: 12px;
  }
  .brand-mark__circle {
    width: 170px; height: 170px; border-radius: 50%;
    background: var(--mark-ring);
  }
  .brand-mark__name {
    font-size: 28px; color: var(--ink-light); letter-spacing: 1px;
  }
  .headline {
    position: absolute; top: 400px; left: 0; right: 0; text-align: center;
  }
  .headline__main {
    font-family: "Luckiest Guy", "Titan One", cursive;
    font-size: 50px; color: var(--title-gold); line-height: 1;
    white-space: nowrap;
  }
  .headline__sub {
    font-size: 50px; color: var(--title-blue); line-height: 1.1;
    white-space: nowrap;
  }
  .contact {
    position: absolute; top: 620px; left: 50px; right: 50px;
    display: flex; justify-content: space-between;
    font-size: 32px; line-height: 1.3;
  }
  .contact__address { text-align: right; }
  .front-email {
    position: absolute; top: 790px; width: 100%; text-align: center; font-size: 28px;
  }
  .front-web {
    position: absolute; top: 840px; width: 100%; text-align: center; font-size: 34px;
  }

  /* Back */
  .back-sky {
    position: absolute; inset: 0 0 370px 0;
    background: linear-gradient(180deg, var(--sky-top), var(--sky-bottom));
  }
  .back-photo {
    position: absolute; left: 0; right: 0; bottom: 0; height: 370px;
    background: linear-gradient(180deg, var(--sea-top) 0%, #27468f 40%, var(--sea-bottom) 100%);
  }
  .back-title {
    position: absolute; top: 90px; width: 100%; text-align: center;
    font-size: 72px; letter-spacing: 1px;
  }
  .social {
    position: absolute; top: 205px; left: 0; right: 0;
    display: flex; justify-content: center; gap: 40px;
  }
  .social__item { display: flex; align-items: center; gap: 10px; font-size: 36px; }
  .social__square { width: 28px; height: 28px; background: var(--ink-light); }
  .tag-intro {
    position: absolute; top: 290px; width: 100%; text-align: center; font-size: 40px;
  }
  .tag-handles {
    position: absolute; top: 360px; width: 100%; text-align: center;
    font-size: 38px; line-height: 1.2;
  }
  .back-web {
    position: absolute; top: 760px; width: 100%; text-align: center; font-size: 38px;
  }
</style>
</head>
<body>
  <section class="card card--front">
    <div class="front-photo" role="img" aria-label="Misty subtropical rainforest with ferns and mossy trees"></div>
    <div class="brand-mark">
      <div class="brand-mark__circle"></div>
      <div class="brand-mark__name">Kestrel Point Wildland Tours</div>
    </div>
    <div class="headline">
      <div class="headline__main">KESTREL POINT</div>
      <div class="headline__sub">Wildland Tours</div>
    </div>
    <div class="contact">
      <div class="contact__person">
        <div>Director</div>
        <div>Colin Warbeck</div>
        <div>+61 2 5550 1847</div>
      </div>
      <div class="contact__address">
        <div>PO Box 71</div>
        <div>Marlin Cove</div>
        <div>NSW 2471</div>
      </div>
    </div>
    <div class="front-email">info@kestrelpointtours.com</div>
    <div class="front-web">www.kestrelpointtours.com</div>
  </section>

  <section class="card card--back">
    <div class="back-sky"></div>
    <div class="back-photo" role="img" aria-label="Two smiling snorkellers in masks in the open sea"></div>
    <div class="back-title">Taking pictures?</div>
    <div class="social">
      <div class="social__item"><span class="social__square"></span>Friendwall</div>
      <div class="social__item"><span class="social__square"></span>Pixlane</div>
    </div>
    <div class="tag-intro">Tag us in your pictures with</div>
    <div class="tag-handles">
      <div>#kpwildtours</div>
      <div>@kpwildtours</div>
    </div>
    <div class="back-web">www.kestrelpointtours.com</div>
  </section>
</body>
</html>
```